Corvane Supplies Business Card

Professional business card that stand out to our potential customers. Front and back with clean modern design

Industry/Entity Type

Oil and gas

Contact Information for Business Card

Name, address, website , office phone and cell number

Requirements
Must have
• Editable files for each employee

```html
<!DOCTYPE html>
<html lang="en">
<head>
<meta charset="utf-8">
<title>Corvane Supplies Business Card</title>
<link rel="stylesheet" href="https://fonts.googleapis.com/css2?family=Montserrat:wght@400;700&family=Open+Sans:wght@400&display=swap">
<style>
  :root {
    --page: #eeecec;
    --card: #ffffff;
    --teal: #06b1d0;
    --teal-soft: rgba(6, 177, 208, 0.55);
    --teal-clear: rgba(6, 177, 208, 0);
    --red: #f20000;
    --ink: #111111;
  }
  * { margin: 0; padding: 0; box-sizing: border-box; }
  html, body { width: 1200px; height: 1200px; overflow: hidden; }
  body { background: var(--page); position: relative; font-family: "Montserrat", sans-serif; }

  .card {
    position: absolute;
    height: 388px;
    background: var(--card);
    overflow: hidden;
  }
  .card--front { left: 266px; top: 196px; width: 645px; }
  .card--back  { left: 265px; top: 631px; width: 650px; }

  .accent {
    position: absolute;
    width: 256px;
    height: 164px;
  }
  .accent--top {
    left: 0; top: 0;
    background: linear-gradient(200deg, var(--teal-soft) 0%, var(--teal-clear) 75%);
  }
  .accent--bottom {
    right: 0; bottom: 0;
    background: linear-gradient(20deg, var(--teal-soft) 0%, var(--teal-clear) 75%);
  }

  /* Front */
  .brand {
    position: absolute;
    display: flex;
    align-items: center;
  }
  .brand--front {
    left: 182px;
    top: 109px;
    gap: 14px;
  }
  .brand__mark { width: 82px; height: 82px; background: var(--red); flex: none; }
  .brand__name {
    font-family: "Montserrat", sans-serif;
    font-weight: 700;
    color: var(--red);
    text-transform: uppercase;
    white-space: nowrap;
  }
  .brand--front .brand__name { font-size: 36px; line-height: 1.08; }
  .tagline {
    position: absolute;
    left: 0; right: 0;
    top: 245px;
    text-align: center;
    font-family: "Open Sans", sans-serif;
    font-size: 15px;
    letter-spacing: 0.42em;
    color: var(--ink);
  }

  /* Back */
  .brand--back {
    top: 113px;
    left: 55px;
    width: 202px;
    flex-direction: column;
    gap: 38px;
  }
  .brand--back .brand__mark { width: 78px; height: 86px; }
  .brand--back .brand__name { font-size: 19px; line-height: 23px; text-align: center; }

  .person {
    position: absolute;
    right: 41px;
    top: 59px;
    text-align: right;
  }
  .person__name { font-weight: 700; color: var(--red); font-size: 33px; line-height: 1; letter-spacing: 0.01em; }
  .person__role { font-weight: 400; color: var(--ink); font-size: 19px; line-height: 1.2; margin-top: 2px; }

  .contacts {
    position: absolute;
    right: 41px;
    top: 143px;
    list-style: none;
    text-align: right;
    color: var(--ink);
    font-size: 19px;
    line-height: 24px;
  }
  .contacts__item { display: flex; justify-content: flex-end; align-items: center; gap: 10px; }
  .contacts__item--plain { padding-right: 25px; }
  .contacts__icon { width: 15px; height: 15px; flex: none; }
</style>
</head>
<body>

<section class="card card--front" aria-label="Card front">
  <div class="accent accent--top" role="img" aria-label="Teal flowing wave decoration"></div>
  <div class="accent accent--bottom" role="img" aria-label="Teal flowing wave decoration"></div>
  <div class="brand brand--front">
    <span class="brand__mark"></span>
    <span class="brand__name">Corvane<br>Supplies</span>
  </div>
  <p class="tagline">your web / email address here</p>
</section>

<section class="card card--back" aria-label="Card back">
  <div class="accent accent--top" role="img" aria-label="Teal flowing wave decoration"></div>
  <div class="accent accent--bottom" role="img" aria-label="Teal flowing wave decoration"></div>

  <div class="brand brand--back">
    <span class="brand__mark"></span>
    <span class="brand__name">Corvane Supplies</span>
  </div>

  <div class="person">
    <p class="person__name">NAME HERE</p>
    <p class="person__role">Graphic Designer</p>
  </div>

  <ul class="contacts">
    <li class="contacts__item">+000 00 00 00 00
      <svg class="contacts__icon" viewBox="0 0 16 16" aria-hidden="true"><circle cx="8" cy="8" r="8" fill="var(--teal)"/><circle cx="8" cy="6" r="2.2" fill="#fff"/><path d="M4.3,12 C4.6,9.4 11.4,9.4 11.7,12 Z" fill="#fff"/></svg>
    </li>
    <li class="contacts__item">+000 00 00 00 00
      <svg class="contacts__icon" viewBox="0 0 16 16" aria-hidden="true"><circle cx="8" cy="8" r="8" fill="var(--teal)"/><path d="M6,4.2 L7,6.4 L6.2,7.2 C6.7,8.3 7.7,9.3 8.8,9.8 L9.6,9 L11.8,10 L11.3,11.5 C8,11.5 4.5,8 4.5,4.7 Z" fill="#fff"/></svg>
    </li>
    <li class="contacts__item">www.your website here
      <svg class="contacts__icon" viewBox="0 0 16 16" aria-hidden="true"><circle cx="8" cy="8" r="8" fill="var(--teal)"/><g fill="none" stroke="#fff" stroke-width="0.9"><circle cx="8" cy="8" r="4"/><ellipse cx="8" cy="8" rx="1.7" ry="4"/><path d="M4,8 H12"/></g></svg>
    </li>
    <li class="contacts__item">23 anywhere st, any city
      <svg class="contacts__icon" viewBox="0 0 16 16" aria-hidden="true"><circle cx="8" cy="8" r="8" fill="var(--teal)"/><path d="M8,12.5 C6,10 5,8.6 5,7 A3,3 0 0 1 11,7 C11,8.6 10,10 8,12.5 Z" fill="#fff"/><circle cx="8" cy="7" r="1.1" fill="var(--teal)"/></svg>
    </li>
    <li class="contacts__item contacts__item--plain">Po.Box - 00</li>
  </ul>
</section>

</body>
</html>
```